Business Cards + Flyer + Letterhead for Care Recruitment Agency

We are a recruitment agency for the health & care sector. We need designs made for business cards, A5 double-sided flyer, and a letterhead template.

Our branding message is professionalism, care, compassion, expertise. We are experts in recruitment for the care & health industry.

Our logo source files and colours are here - https://www.filevault-example.net/sh/qplr82nvzkx/BBKdLm4ORTe93pWqHnZxYa?dl=0

For the business card, I have attached an example we like. We want a vertical business card design, something very similar to the example given. The design should match our logo in terms of brand colors. On one side should be our logo, our website (www.penhollowbrook.co.uk) and Care Recruitment Specialists written somewhere visible that fits, between our logo and the website at the bottom. On the other side should be our details.

Details on the front:

Logo with slogan
Care Recruitment Specialists
www.penhollowbrook.co.uk

Details on the back:

Marcus Ellory
Managing Director

Rowan Court, 41-47 Tillwick St, Birmingham, B9 7QX
07612 459073
marcus@penhollowbrook.co.uk
www.penhollowbrook.co.uk

Deirdre Penhollow
Business Development Director

07831 204968
deirdre@penhollowbrook.co.uk
www.penhollowbrook.co.uk

For the A5 flyer, I have attached some pictures we've used for the website, which could be used for the flyer as well. To get a better idea of our branding, please visit our website - https://penhollowbrook.co.uk/

The text for the flyer is also attached.

Finally, the letterhead template should be a docx template with our logo and our identifiable branding (the same shapes and matching colours you will come up with for the business cards and flyer).

```html
<!DOCTYPE html>
<html lang="en">
<head>
<meta charset="utf-8">
<title>Penhollow Brook — Letterhead</title>
<link href="https://fonts.googleapis.com/css2?family=Montserrat:wght@300;400;700&family=Mulish:wght@400;500&family=Roboto+Condensed:wght@300;400&display=swap" rel="stylesheet">
<style>
  :root {
    --navy: #1e2a5e;
    --sky: #3ec3ee;
    --ink: #5b5b5b;
    --contact: #1b2a6b;
    --backdrop: #d6d6d6;
    --paper: #ffffff;
  }
  * { margin: 0; padding: 0; box-sizing: border-box; }
  html, body {
    width: 1056px; height: 1200px; overflow: hidden;
    background: var(--backdrop);
  }
  .letterhead {
    position: absolute; left: 104px; top: 0;
    width: 848px; height: 1200px;
    background: var(--paper);
    color: var(--ink);
  }
  .brand {
    position: absolute; left: 80px; top: 128px;
    display: flex; align-items: center; gap: 10px;
  }
  .brand-dot {
    width: 14px; height: 14px; border-radius: 50%;
    background: var(--sky);
  }
  .brand-name {
    font-family: "Montserrat", sans-serif; font-weight: 700;
    font-size: 20px; letter-spacing: 2.6px; color: var(--navy);
  }
  .contact {
    position: absolute; left: 603px; top: 80px;
    font-family: "Mulish", sans-serif; font-size: 13px; font-style: normal;
    color: var(--contact); line-height: 17px;
  }
  .contact-address { margin-bottom: 8px; }
  .contact-line { display: flex; align-items: center; gap: 10px; height: 19.5px; }
  .contact-line svg { width: 14px; height: 14px; flex: none; }
  .letter-date {
    position: absolute; left: 80px; top: 358px;
    font-family: "Montserrat", sans-serif; font-weight: 300; font-size: 19px;
  }
  .recipient-name {
    position: absolute; left: 80px; top: 392px;
    font-family: "Montserrat", sans-serif; font-weight: 700; font-size: 30px;
    letter-spacing: 0.2px;
  }
  .recipient-title {
    position: absolute; left: 80px; top: 436px;
    font-family: "Montserrat", sans-serif; font-weight: 300; font-size: 19px;
  }
  .letter-body {
    position: absolute; left: 80px; top: 511px; width: 688px;
    font-family: "Roboto Condensed", sans-serif; font-weight: 300;
    font-size: 16.5px; line-height: 29.5px; text-align: justify;
  }
  .letter-body p { margin-bottom: 29px; }
  .sign-off {
    position: absolute; left: 80px; top: 962px;
    font-family: "Roboto Condensed", sans-serif; font-weight: 300; font-size: 18px;
  }
  .signature {
    position: absolute; left: 80px; top: 1008px;
    width: 88px; height: 58px; border-radius: 4px;
    background: linear-gradient(135deg, #e9ebf3, #cfd3e4);
  }
  .footer-band {
    position: absolute; left: 0; bottom: 0; width: 848px; height: 31px;
    background: linear-gradient(90deg, var(--sky), var(--navy));
  }
</style>
</head>
<body>
  <main class="letterhead">
    <header>
      <div class="brand">
        <span class="brand-dot"></span>
        <span class="brand-name">PENHOLLOW BROOK</span>
      </div>
      <address class="contact">
        <div class="contact-address">Rowan Court, 41-47<br>Tillwick St, Birmingham, B9 7QX</div>
        <div class="contact-line">
          <svg viewBox="0 0 16 16" aria-hidden="true"><path d="M4 2 L6.5 2 L7.5 5 L5.8 6.3 Q7 9.2 9.7 10.3 L11 8.6 L14 9.6 L14 12 Q13.6 14 11.5 14 Q3 13 2 4.5 Q2 2 4 2Z" fill="none" stroke="var(--sky)" stroke-width="1.5"/></svg>
          <span>07612 459073</span>
        </div>
        <div class="contact-line">
          <svg viewBox="0 0 16 16" aria-hidden="true"><rect x="1" y="3.5" width="14" height="9.5" fill="var(--sky)"/><path d="M1 3.5 L8 9 L15 3.5" fill="none" stroke="#fff" stroke-width="1.2"/></svg>
          <span>marcus@penhollowbrook.co.uk</span>
        </div>
        <div class="contact-line">
          <svg viewBox="0 0 16 16" aria-hidden="true"><g fill="none" stroke="var(--sky)" stroke-width="1.1"><circle cx="8" cy="8" r="6.5"/><ellipse cx="8" cy="8" rx="2.8" ry="6.5"/><path d="M1.5 8 H14.5"/></g></svg>
          <span>www.penhollowbrook.co.uk</span>
        </div>
      </address>
    </header>

    <div class="letter-date">10 December, 2020</div>
    <h1 class="recipient-name">DANIEL HARTWELL</h1>
    <div class="recipient-title">Cheif Executive Officer</div>

    <section class="letter-body">
      <p>Contrary to popular belief, Lorem Ipsum is not simply random text. It has roots in a piece of classical Latin literature from 45 BC, making it over 2000 years old. Edward Lindqvist, a Latin professor at Ashcombe College in Vermont, looked up one of the more obscure Latin words, consectetur.</p>
      <p>Lorem Ipsum comes from sections 1.10.32 and 1.10.33 of "de Finibus Bonorum et Malorum" (The Extremes of Good and Evil) by Aurelian, written in 45 BC. This book is a treatise on the theory of ethics, very popular during the Renaissance. The first line of Lorem Ipsum.</p>
      <p>The standard chunk of Lorem Ipsum used since the 1500s is reproduced below for those interested. Sections 1.10.32 and 1.10.33 from "de Finibus Bonorum et Malorum" by Aurelian are also reproduced in their exact original.</p>
      <p>The standard chunk of Lorem Ipsum used since the 1500s is reproduced below for those interested.</p>
    </section>

    <div class="sign-off">Best Regards</div>
    <div class="signature" role="img" aria-label="Handwritten signature of the sender"></div>

    <div class="footer-band" role="img" aria-label="Decorative footer stripes in sky blue and navy"></div>
  </main>
</body>
</html>
```